■ 依頼の目的/概要

名刺サイズのフライヤー(両面カラー)のデザイン

当店HP : http://www.kiravo-nail.com/

■ フライヤーに記載する情報

表面:店名/住所/電話/URL/Mail/営業時間/地図
裏面:キャッチコピー(ゆび先にも大人の「キレイ」磨き
もっと美しく もっと輝く)
特典メニュー:ジェルネイルお試しコース
通常 5,250円 →  2,980円
甘皮処理+長さ調整+ジェルネイル(カラー1色)
ご新規様初回限定とさせて頂きます

※その他コースメニューございます
↑表現はお任せします

裏表どちらかの面に当店ロゴマーク

■ デザインへの要望

ネイルサロン(ターゲットは女性のみ)のため、女心をくすぐる、つい手にとってしまうようなオシャレなデザインを希望します。

■ 納品ファイルの希望

イラストレーター形式

■ 進め方

弊社の希望するイメージに近い提案を1つ(場合によって複数)選択させて頂きます。希望に近づけるために、修正要望を個別にさせて頂くこともあります。コンペ方式のため、修正後に当選されない場合も、どうかご了承ください。

■ その他/注意点

選択させて頂いたデザインの著作権(財産権)等の扱いはBodrix利用規約に従い、弊社に譲渡をお願いします。フォントや画像素材などを利用する場合は上記利用用途に使用できることを確認し、第三者の知的財産権等に注意して下さい。
フライヤーに写真画像をのせる場合は当店HP(http://www.kiravo-nail.com/)もしくは当店ブログ(http://kiravo-blog.com/)の画像を使用して頂いて構いません。
可能であれば、写真入りのデザインと写真無しのデザインを提案して頂けると幸いです。

ちなみに、フライヤーは近隣の美容室や飲食店等のレジ付近に置いて頂くものですので、女性の方の目を引き、手にとって頂けるようなオシャレなデザインを希望致します。
サイズが名刺サイズと小さいので、あまり細かい文字を多くは入れなくても良いです。

何卒、宜しくお願い致します。
たくさんのご提案ありがとうございます。
以下、変更点&補足事項ですので宜しくお願い致します。

表面は白抜きのロゴマークを中心に、キャッチコピーを入れて下さい。
そして周辺に何か柄などのデザインを入れて欲しいです。

裏面は住所等の情報+得点メニュー+ネイル(手)の写真を入れて下さい。

締め切りを延長させて頂きますので、再度ご提案頂けますよう、何卒宜しくお願い致します。
たくさんのデザインをご提案下さってありがとうございます。
気になっているデザインがいくつかありますので、非常に迷っております。
選定にまだ時間がかかりそうですので、締め切りを延長させて頂きます。
可能であれば、裏面のデザインを含め、再度ご提案下さると幸いです。
(現在のご提案分の気に入っている箇所と、再度ご提案頂いて気に行った箇所をミックスしたりと、私が選定しやすくなるので…。)
何卒、宜しくお願い致します。
たくさんのご提案ありがとうございます。
フライヤーは現在選定中でございます。

別件ですが、「スナックの名刺」の依頼も開始しましたので、是非ご提案頂きますよう宜しくお願い致します。

全体的なバランス、そして私好みのデザインでしたので決定させて頂きました。

皆様からたくさん素敵なご提案を頂き、最後の最後まで選定に迷いました。ご提案下さいました皆様に感謝致します。ありがとうございました。
そしてこれから先も、名刺やチラシ等作成予定ですので、また宜しくお願い致します。

```html
<!DOCTYPE html>
<html lang="ja">
<head>
<meta charset="utf-8">
<title>Kiravo nail salon — flyer proposals</title>
<link href="https://fonts.googleapis.com/css2?family=Cormorant+Garamond:ital,wght@0,500;1,500&family=Noto+Serif+JP:wght@500&display=swap" rel="stylesheet">
<style>
  :root{
    --sheet:#ffffff;
    --card-dark:#7e1744;
    --card-mid:#9c2358;
    --card-light:#b2356a;
    --ink:#ffffff;
    --ink-soft:rgba(255,255,255,.82);
    --ornament:rgba(255,255,255,.55);
  }
  *{margin:0;padding:0;box-sizing:border-box}
  html,body{width:849px;height:1200px;overflow:hidden;background:var(--sheet)}
  .sheet{position:relative;width:849px;height:1200px}
  .card{
    position:absolute;overflow:hidden;color:var(--ink);
    background:radial-gradient(ellipse at 50% 45%,var(--card-light) 0%,var(--card-mid) 45%,var(--card-dark) 100%);
    box-shadow:0 1px 3px rgba(0,0,0,.25);
    display:flex;flex-direction:column;align-items:center;text-align:center;
  }
  .card--portrait{width:249px;height:368px;padding-top:58px}
  .card--landscape{width:368px;height:227px;padding-top:34px}
  .card--p1{left:161px;top:127px}
  .card--p2{left:439px;top:127px}
  .card--l1{left:240px;top:594px}
  .card--l2{left:240px;top:849px}
  .catch{font-family:"Noto Serif JP",serif;font-weight:500;font-size:10.5px;line-height:1.7;letter-spacing:.02em}
  .card--landscape .catch{font-size:9.5px}
  .brand{margin-top:62px;display:flex;flex-direction:column;align-items:center}
  .card--landscape .brand{margin-top:22px}
  .brand__name{font-family:"Cormorant Garamond",serif;font-weight:500;font-size:46px;line-height:1;letter-spacing:.01em;color:var(--ink)}
  .card--landscape .brand__name{font-size:42px}
  .brand__sub{font-family:"Cormorant Garamond",serif;font-weight:500;font-size:11px;letter-spacing:.22em;margin-top:4px;color:var(--ink-soft)}
  .url{font-family:"Cormorant Garamond",serif;font-weight:500;font-size:9.5px;letter-spacing:.06em;color:var(--ink-soft);margin-top:auto;margin-bottom:80px}
  .card--landscape .url{margin-bottom:20px}
  .ornament{position:absolute;width:46px;height:46px;background:radial-gradient(circle at 30% 30%,var(--ornament),rgba(255,255,255,.12) 70%,transparent 72%)}
  .card--landscape .ornament{width:40px;height:40px}
  .ornament--tl{left:6px;top:6px}
  .ornament--tr{right:6px;top:6px}
  .ornament--bl{left:6px;bottom:6px}
  .ornament--br{right:6px;bottom:6px}
</style>
</head>
<body>
<main class="sheet">

  <section class="card card--portrait card--p1">
    <div class="ornament ornament--tr" role="img" aria-label="White filigree corner ornament"></div>
    <div class="ornament ornament--bl" role="img" aria-label="White filigree corner ornament"></div>
    <p class="catch">ゆび先にも大人の「キレイ」磨きを<br>もっと美しく、もっと輝く。</p>
    <div class="brand"><span class="brand__name">Kiravo</span><span class="brand__sub">-nail salon-</span></div>
    <p class="url">www.kiravo-nail.com</p>
  </section>

  <section class="card card--portrait card--p2">
    <div class="ornament ornament--tl" role="img" aria-label="White filigree corner ornament"></div>
    <div class="ornament ornament--br" role="img" aria-label="White filigree corner ornament"></div>
    <p class="catch">ゆび先にも大人の「キレイ」磨きを<br>もっと美しく、もっと輝く。</p>
    <div class="brand"><span class="brand__name">Kiravo</span><span class="brand__sub">-nail salon-</span></div>
    <p class="url">www.kiravo-nail.com</p>
  </section>

  <section class="card card--landscape card--l1">
    <div class="ornament ornament--tl" role="img" aria-label="White filigree corner ornament"></div>
    <div class="ornament ornament--br" role="img" aria-label="White filigree corner ornament"></div>
    <p class="catch">ゆび先にも大人の「キレイ」磨きをもっと美しく、もっと輝く。</p>
    <div class="brand"><span class="brand__name">Kiravo</span><span class="brand__sub">-nail salon-</span></div>
    <p class="url">www.kiravo-nail.com</p>
  </section>

  <section class="card card--landscape card--l2">
    <div class="ornament ornament--tl" role="img" aria-label="White filigree corner ornament"></div>
    <div class="ornament ornament--tr" role="img" aria-label="White filigree corner ornament"></div>
    <div class="ornament ornament--bl" role="img" aria-label="White filigree corner ornament"></div>
    <div class="ornament ornament--br" role="img" aria-label="White filigree corner ornament"></div>
    <p class="catch">ゆび先にも大人の「キレイ」磨きをもっと美しく、もっと輝く。</p>
    <div class="brand"><span class="brand__name">Kiravo</span><span class="brand__sub">-nail salon-</span></div>
    <p class="url">www.kiravo-nail.com</p>
  </section>

</main>
</body>
</html>
```